An Agro-Processor Needs a Packaging Design

We need packaging designs for a range of dried fruits and jams with a family look. The line-up has five variants of dried fruits and five variants of jams (the designs to include front and back of the packaging). The entire range will be marketed under the 'Petalvyn' brand name - please find the logo attached (the logo has a lock-up with the tagline). The packaging format for the dried fruits are resealable stand-up pouches and the jams are glass bottles - please find attached pictures of the packaging formats for reference.

Please find inspiration boards for the packaging design. Also find attached inspiration board for the design style required for the back of the dried fruit packaging.

For the dried fruit packaging, we need to develop a seal that conveys organic and sugar-free claims (please find attached example of a seal)

Target Market(s)

Organic and natural living enthusiasts who would pay a premium to get the best for them and their families

Industry/Entity Type

Food Production

Font styles to use
Sans Serif
Script

Colors

Designer to choose colors to be used in the design.

Requirements
Must have
• - The brand name 'petalvyn' is inspired by the abundance of nature in Africa, it also connotes organic, natural, freshness, delicateness, airiness, sophistication and premium and therefore the design should project these values
• - The design styling to be fun, modern and 'simplistic'
• - Please find below the packaging copy for both dried fruits and jams
• DRIED FRUIT FRONT PACKAGING:
• LOGO: Petalvyn - Sharing Earth's Warmth
• FIVE VARIANT NAMES: Plucky Pineapple | Dreamy Mango | Jolly Banana | Dapper Papaya | Breezy Jackfruit
• Dried
• DEVELOP A SEAL: 100% Organic | No Added Sugar (please see example attached)
• Ugandan Origin
• Net Weight: 100g
• DRIED FRUIT BACK COPY:
• Nature's best tasting fruits are also the healthiest which is why we have made it our mission to spread nature's love! Nourished by the tropical rains on the sun-drenched soils of Africa and cultivated by the caring hands of the local farmers, our organic range of dried fruits are nutrient-dense, high in fiber and rich in minerals. Enjoy them in your salads and cereals or simply relish them as a snack! They are diet-friendly if eaten in moderation and are a natural source of energy.
• VISUAL: Stack of Fruit Visual with arrows, each with the following claims (see examples attached in the inspiration boards):
• - 100% Organic
• - No Added Sugar
• - Nutrient-Dense
• - High in Fiber
• - Rich in Minerals
• INCLUDE: Nutritional Facts Table
• Ingredients: Mango - contains 100% fruit with no added sugars, preservatives, additives, colorings or flavorings.
• Reseal the pack to maintain freshness. Store in a cool and dry place.
• INCLUDE SPACE FOR: Batch Code / Expiry Date
• Barcode
• Produced by: Temari Food Industries, P. O. Box XXXXX, Kampala - Uganda.
• Find out more about us:
• Telephone: +XXX-XXX-XXXXXX
• Email: Info@TemariFoodIndustriez.com
• www.Chatterbook.net/Petalvyn
• JAM FRONT COPY:
• FIVE VARIANT NAMES: Plucky Pineapple with a Hint of Ginger | Dreamy Mango with a Kiss of Vanilla | Jolly Banana with a Twist of Chocolate | Dapper Papaya with a Pinch of Cardamon | Breezy Jackfruit with a Touch of Cinnamon
• Jam
• Ugandan Origin
• Net Weight: 400g
• JAM BACK COPY:
• Nature's best tasting fruits are also the healthiest which is why we have made it our mission to spread nature's love! Our range of jams come from fruits that have been nourished by the tropical rains on the sun-drenched soils of Africa and have been cultivated by the caring hands of the local farmers. We pride ourselves on making sure that the jams taste as delicious and look as natural as the perfectly ripened fruit! We then make it even better by pairing it with a hint of spice! Enjoy them in your breakfast or use them as a filling in baking.
• Ingredients: Mango, citric acid, sugar, pectin, vanilla
• Barcode
• Find out more about us:

```html
<!DOCTYPE html>
<html lang="en">
<head>
<meta charset="utf-8">
<title>Petalvyn Dried Mango Pouch – Front</title>
<link rel="stylesheet" href="https://fonts.googleapis.com/css2?family=Oswald:wght@400;500&family=Poppins:wght@400;500;600&family=Itim&display=swap">
<style>
  :root {
    --page: #efece6;
    --pouch: #fbfbfb;
    --pouch-edge: #e4e4e4;
    --brown: #4a3a36;
    --pink: #e0505e;
    --lavender: #a99bd0;
    --lavender-line: #ffffff;
    --organic: #7cc242;
    --sugar: #f0952b;
    --mango: #f1a23a;
    --green: #4e9b2f;
    --ink: #2e2e2e;
    --white: #ffffff;
  }
  * { margin: 0; padding: 0; box-sizing: border-box; }
  html, body { width: 1200px; height: 1200px; overflow: hidden; }
  body {
    background: var(--page);
    display: flex;
    align-items: center;
    justify-content: center;
    font-family: "Poppins", sans-serif;
  }
  .pouch {
    position: relative;
    width: 760px;
    height: 1080px;
    background: var(--pouch);
    border: 1px solid var(--pouch-edge);
    border-radius: 6px 6px 40px 40px;
    box-shadow: 0 10px 30px rgba(0,0,0,0.08);
  }
  .pouch__zip {
    position: absolute;
    top: 70px; left: 0; right: 0;
    height: 2px;
    background: var(--pouch-edge);
  }
  .brand {
    position: absolute;
    top: 150px; left: 0; right: 0;
    text-align: center;
  }
  .brand__name {
    display: inline-flex;
    align-items: center;
    gap: 14px;
    font-family: "Poppins", sans-serif;
    font-weight: 600;
    font-size: 104px;
    line-height: 1;
    color: var(--brown);
    letter-spacing: -1px;
  }
  .brand__dot {
    width: 22px; height: 22px;
    border-radius: 50%;
    background: var(--pink);
  }
  .brand__tagline {
    margin-top: 10px;
    font-family: "Itim", cursive;
    font-size: 32px;
    color: var(--pink);
    letter-spacing: 1px;
  }
  .variants {
    position: absolute;
    top: 400px; left: 0; right: 0;
    height: 122px;
    background: var(--lavender);
    display: flex;
    flex-direction: column;
    align-items: center;
    justify-content: center;
    border-top: 3px solid var(--lavender);
    border-bottom: 3px solid var(--lavender);
    box-shadow: inset 0 8px 0 -4px var(--lavender-line), inset 0 -8px 0 -4px var(--lavender-line);
  }
  .variants__line {
    font-family: "Oswald", sans-serif;
    font-size: 30px;
    color: var(--white);
    letter-spacing: 1px;
    line-height: 1.3;
  }
  .claims {
    position: absolute;
    top: 560px; left: 0; right: 0;
    height: 160px;
  }
  .seal {
    position: absolute;
    top: 20px;
    width: 120px; height: 120px;
    border-radius: 50%;
    display: flex;
    flex-direction: column;
    align-items: center;
    justify-content: center;
    color: var(--white);
    text-align: center;
    line-height: 1;
    box-shadow: inset 0 0 0 9px currentColor;
  }
  .seal::before {
    content: "";
    position: absolute;
    inset: 9px;
    border-radius: 50%;
    border: 2px solid var(--white);
  }
  .seal--organic { left: 92px; background: var(--organic); box-shadow: none; }
  .seal--sugar { right: 70px; background: var(--sugar); box-shadow: none; }
  .seal__top {
    font-family: "Oswald", sans-serif;
    font-weight: 400;
    font-size: 30px;
  }
  .seal--sugar .seal__top {
    font-size: 20px;
    letter-spacing: 0.5px;
  }
  .seal__bottom {
    margin-top: 4px;
    font-family: "Poppins", sans-serif;
    font-weight: 400;
    font-size: 19px;
  }
  .product {
    position: absolute;
    top: 0; left: 0; right: 0;
    text-align: center;
  }
  .product__type {
    font-family: "Oswald", sans-serif;
    font-weight: 500;
    font-size: 118px;
    line-height: 1;
    color: var(--brown);
  }
  .product__origin {
    margin-top: 14px;
    font-size: 25px;
    font-weight: 500;
    color: var(--pink);
    letter-spacing: 1px;
  }
  .fruit-art {
    position: absolute;
    top: 760px; left: 50%;
    transform: translateX(-50%);
    width: 300px; height: 170px;
    border-radius: 50% 45% 50% 48%;
    background: radial-gradient(ellipse at 40% 40%, #f7b44c, var(--mango) 60%, #e38a24);
  }
  .ingredients {
    position: absolute;
    top: 960px; left: 120px; right: 120px;
    text-align: center;
    font-size: 14px;
    font-weight: 500;
    color: var(--ink);
    line-height: 1.35;
    letter-spacing: 0.3px;
  }
  .net-weight {
    position: absolute;
    top: 1005px; left: 0; right: 0;
    text-align: center;
    font-size: 44px;
    font-weight: 600;
    color: var(--green);
  }
</style>
</head>
<body>
  <main class="pouch">
    <div class="pouch__zip"></div>

    <header class="brand">
      <div class="brand__name">petalvyn<span class="brand__dot"></span></div>
      <p class="brand__tagline">Sharing Earth's Warmth</p>
    </header>

    <section class="variants">
      <p class="variants__line">PLUCKY PINEAPPLE | DREAMY MANGO | JOLLY BANANA |</p>
      <p class="variants__line">DAPPER PAPAYA | BREEZY JACKFRUIT</p>
    </section>

    <section class="claims">
      <div class="seal seal--organic">
        <span class="seal__top">100%</span>
        <span class="seal__bottom">Organic</span>
      </div>
      <div class="product">
        <h1 class="product__type">DRIED</h1>
        <p class="product__origin">UGANDAN ORIGIN</p>
      </div>
      <div class="seal seal--sugar">
        <span class="seal__top">NO ADDED</span>
        <span class="seal__bottom">Sugar</span>
      </div>
    </section>

    <div class="fruit-art" role="img" aria-label="Illustrated mango with a green leaf, surrounded by small pastel flowers and leaves"></div>

    <p class="ingredients">MANGO – CONTAINS 100% FRUIT WITH NO ADDED SUGARS, PRESERVATIVES, ADDITIVES, COLORINGS OR FLAVORINGS.</p>

    <p class="net-weight">100g</p>
  </main>
</body>
</html>
```